Card for Real Estate Developer

We need a business card design for a Real Estate Development company based in Texas. We focus on retail, apartment and residential development. Our target is predominantly investors looking to us to place their money properly to achieve a significant return. On the other side we sell our services to large retailers as their preferred developer assisting them in locating, building and leasing their real estate.

Target Market(s)

Investors

Industry/Entity Type

Real Estate Development

Contact Information for Business Card

Would like to stay within the company color scheme, while keeping the design moderately simple.

Font styles to use
Other font styles liked:
• per attached document

Requirements
Must have
• Name
• Phone
• Email
• Website
• Logo Prominently Displayed
• Stay within the colors provided in the attached document

```html
<!DOCTYPE html>
<html lang="en">
<head>
<meta charset="utf-8">
<title>Halvern Development – Business Card</title>
<link rel="stylesheet" href="https://fonts.googleapis.com/css2?family=Cinzel:wght@500&family=Open+Sans:wght@400&display=swap">
<style>
  :root {
    --page: #e4e4e2;
    --card: #f3f3f3;
    --brand-blue: #5094b9;
    --ink: #2f2f2f;
    --ink-soft: #3f3f3f;
    --rule: #4a4a4a;
  }
  * { box-sizing: border-box; margin: 0; padding: 0; }
  html, body { width: 1200px; height: 909px; overflow: hidden; }
  body {
    background: var(--page);
    display: flex;
    flex-direction: column;
    align-items: center;
    justify-content: center;
    gap: 40px;
  }
  .card {
    position: relative;
    width: 640px;
    height: 366px;
    background: var(--card);
    box-shadow: 0 6px 18px rgba(0,0,0,0.18);
    overflow: hidden;
  }
  .wordmark {
    display: flex;
    align-items: center;
    gap: 14px;
    font-family: "Cinzel", serif;
    font-weight: 500;
    color: var(--brand-blue);
    letter-spacing: 0.06em;
    line-height: 1.1;
  }
  .wordmark-square {
    background: var(--brand-blue);
    flex: none;
  }
  .card-front .wordmark {
    position: absolute;
    left: 50%;
    top: 50%;
    transform: translate(-50%, -50%);
    font-size: 38px;
    white-space: nowrap;
  }
  .card-front .wordmark-square { width: 30px; height: 30px; }

  .card-back .contact-name {
    position: absolute;
    left: 46px;
    top: 34px;
    font-family: "Cinzel", serif;
    font-weight: 500;
    font-size: 27px;
    color: var(--brand-blue);
    letter-spacing: 0.04em;
  }
  .card-back .contact-role {
    position: absolute;
    left: 46px;
    top: 70px;
    font-family: "Open Sans", sans-serif;
    font-size: 15px;
    color: var(--ink);
  }
  .contact-list {
    position: absolute;
    left: 46px;
    top: 142px;
    list-style: none;
    font-family: "Open Sans", sans-serif;
    font-size: 18px;
    color: var(--ink);
  }
  .contact-list li {
    display: flex;
    align-items: center;
    gap: 12px;
    height: 27px;
  }
  .contact-icon { width: 17px; height: 17px; flex: none; }
  .wave-band {
    position: absolute;
    left: 0;
    bottom: 0;
    width: 640px;
    height: 366px;
  }
  .card-back .wordmark {
    position: absolute;
    right: 34px;
    top: 196px;
    font-size: 24px;
    flex-direction: column;
    align-items: flex-end;
    gap: 4px;
    text-align: right;
  }
  .card-back .wordmark-square { width: 22px; height: 22px; }
</style>
</head>
<body>

  <section class="card card-front" aria-label="Card front">
    <div class="wordmark">
      <span class="wordmark-square"></span>
      <span class="wordmark-name">Halvern Development</span>
    </div>
  </section>

  <section class="card card-back" aria-label="Card back">
    <svg class="wave-band" viewBox="0 0 640 366" aria-hidden="true">
      <path d="M0 238 C 120 190, 230 250, 360 290 C 460 320, 560 328, 640 318 L640 366 L0 366 Z" fill="var(--brand-blue)"/>
      <path d="M0 238 C 120 190, 230 250, 360 290 C 460 320, 560 328, 640 318" fill="none" stroke="var(--rule)" stroke-width="3"/>
    </svg>

    <h1 class="contact-name">Reid Callow</h1>
    <p class="contact-role">Director</p>

    <ul class="contact-list">
      <li>
        <svg class="contact-icon" viewBox="0 0 17 17" aria-hidden="true">
          <rect width="17" height="17" rx="2" fill="var(--brand-blue)"/>
          <rect x="5.5" y="2.5" width="6" height="12" rx="1" fill="none" stroke="#fff" stroke-width="1.3"/>
          <circle cx="8.5" cy="12.3" r="0.9" fill="#fff"/>
        </svg>
        <span>0412 555 318</span>
      </li>
      <li>
        <svg class="contact-icon" viewBox="0 0 17 17" aria-hidden="true">
          <rect width="17" height="17" rx="2" fill="var(--brand-blue)"/>
          <rect x="3" y="5" width="11" height="7.5" fill="none" stroke="#fff" stroke-width="1.2"/>
          <path d="M3 5 L8.5 9.3 L14 5" fill="none" stroke="#fff" stroke-width="1.2"/>
        </svg>
        <span>hello@halverndev.com</span>
      </li>
      <li>
        <svg class="contact-icon" viewBox="0 0 17 17" aria-hidden="true">
          <rect width="17" height="17" rx="2" fill="var(--brand-blue)"/>
          <circle cx="8.5" cy="8.5" r="5" fill="none" stroke="#fff" stroke-width="1.2"/>
          <ellipse cx="8.5" cy="8.5" rx="2.2" ry="5" fill="none" stroke="#fff" stroke-width="1"/>
          <line x1="3.5" y1="8.5" x2="13.5" y2="8.5" stroke="#fff" stroke-width="1"/>
        </svg>
        <span>www.halverndev.com</span>
      </li>
    </ul>

    <div class="wordmark">
      <span class="wordmark-square"></span>
      <span class="wordmark-name">Halvern<br>Development</span>
    </div>
  </section>

</body>
</html>
```